Flyer Design for Cyber Security - Half-Fold Brochure

We are looking for a design to our company.
The text speaks about cyber security and ways to defend from cyber attacks.
We will provide the text and guidelines.
We ask to receive the source files (.ai and PDF)
For more questions, feel free to contacts us at: marketing@tovrel.example
Thanks!
Updates

Project Deadline Extended
Reason: Deadline will be extended by 5 Days.

Target Market(s)

C-level executives that will visit QN Shieldcon event.

Industry/Entity Type

Computer Security

Font styles to use
Sans Serif

Colors
f37122
0292cd
ffffff
000000
aaaaaa

Requirements
Must have
• -Nice Icons
• - Graphics and visuals. to take the text and visualised. especially the numbers.
• - Company logo (provided)
• - Velbrisk logo (provided)
• *The full text provided in a word doc.
Nice to have
• I added a few visuals we used in the past. It's the designer's decision whether to use it or not.
• It's a reference for our style, but we are open for new ideas.

```html
<!DOCTYPE html>
<html lang="en">
<head>
<meta charset="utf-8">
<title>Tovrel Security Playbooks – Brochure Spread</title>
<link rel="stylesheet" href="https://fonts.googleapis.com/css2?family=Open+Sans:wght@400;600;700;800&display=swap">
<style>
  :root {
    --orange: #f37122;
    --blue: #0292cd;
    --deep-blue: #127ea8;
    --white: #ffffff;
    --black: #000000;
    --grey: #aaaaaa;
    --text: #4a4a4a;
    --halo: #f4f5f6;
    --halo-inner: #eceef0;
    --page-bg: #e9e9e9;
  }
  html, body { margin: 0; padding: 0; width: 1200px; height: 1200px; overflow: hidden; background: var(--page-bg); }
  .spread {
    position: absolute; left: 0; top: 171px;
    width: 1344px; height: 962px;
    transform: scale(0.89286); transform-origin: 0 0;
    background: var(--white); overflow: hidden;
    font-family: "Open Sans", Arial, sans-serif; color: var(--text);
  }
  .halo { position: absolute; border-radius: 50%; }
  .halo--outer { left: 300px; top: 20px; width: 940px; height: 940px; background: var(--halo); }
  .halo--inner { left: 390px; top: 165px; width: 700px; height: 700px; background: var(--halo-inner); opacity: .6; }
  .banner { position: absolute; background: var(--orange); color: var(--white); box-sizing: border-box; }
  .banner h2 { margin: 0; font-weight: 800; letter-spacing: .5px; text-transform: uppercase; line-height: 1.25; }
  .banner--ransom { left: 22px; top: 34px; width: 626px; height: 132px; padding: 10px 0 0 34px; }
  .banner--ransom h2 { font-size: 29px; }
  .banner--ransom p { margin: 6px 0 0; font-size: 15px; line-height: 1.22; }
  .banner--domain { left: 22px; top: 605px; width: 626px; height: 47px; padding: 6px 0 0 34px; }
  .banner--domain h2 { font-size: 27px; }
  .banner--deface { left: 678px; top: 34px; width: 626px; height: 66px; padding: 13px 0 0 44px; }
  .banner--deface h2 { font-size: 29px; }
  .stat { position: absolute; color: var(--orange); font-size: 18px; line-height: 1; text-align: right; margin: 0; white-space: nowrap; }
  .stat--paid { right: 1062px; top: 202px; }
  .stat--hit { right: 1050px; top: 262px; }
  .stat--sector { right: 919px; top: 332px; }
  .connectors { position: absolute; left: 0; top: 0; }
  .body-copy { position: absolute; margin: 0; font-size: 15px; line-height: 1.24; text-align: justify; letter-spacing: -.35px; }
  .body-copy--ransom { left: 56px; top: 420px; width: 485px; }
  .body-copy--domain { left: 53px; top: 683px; width: 400px; }
  .body-copy--intro { left: 724px; top: 121px; width: 564px; }
  .body-copy--deface { left: 721px; top: 690px; width: 567px; }
  .body-copy--deface p { margin: 0 0 10px; }
  .illustration {
    position: absolute; left: 515px; top: 190px; width: 430px; height: 470px;
    border-radius: 30px;
    background: linear-gradient(160deg, #d8d8d8 0%, #c4c4c4 55%, #a9a9a9 100%);
  }
  .did-you-know {
    position: absolute; right: 74px; top: 323px; margin: 0;
    color: var(--deep-blue); font-size: 29px; line-height: 35.2px; text-align: right; letter-spacing: -.6px;
  }
  .did-you-know strong { font-weight: 700; }
  .network { position: absolute; left: 455px; top: 690px; }
  .footer { position: absolute; left: 0; top: 888px; width: 1344px; height: 74px; background: var(--orange); color: var(--white); }
  .footer__left { position: absolute; left: 167px; top: 22px; font-size: 12.5px; margin: 0; }
  .footer__right { position: absolute; left: 700px; width: 610px; top: 10px; font-size: 10px; text-align: center; line-height: 1.3; margin: 0; }
</style>
</head>
<body>
<main class="spread">
  <div class="halo halo--outer"></div>
  <div class="halo halo--inner"></div>

  <section class="banner banner--ransom">
    <h2>Handling Ransomware/<br>CipherLock Infection</h2>
    <p>Ransomware is growing more advanced, with each evolution<br>becoming more insidious, and damaging:</p>
  </section>

  <div class="illustration" role="img" aria-label="Illustration of a smartphone with a Q1 calendar, reports with charts, and a laptop beside a grey alert card with a masked figure and the words 50.000 attacks"></div>

  <svg class="connectors" width="1344" height="962" aria-hidden="true">
    <g stroke="#f37122" stroke-width="2" fill="none">
      <line x1="307" y1="217" x2="545" y2="217"/>
      <polyline points="331,280 581,280 581,340"/>
      <polyline points="450,348 611,348 611,476"/>
    </g>
    <g fill="#f37122">
      <circle cx="307" cy="217" r="7"/>
      <circle cx="331" cy="280" r="7"/>
      <circle cx="450" cy="348" r="7"/>
    </g>
  </svg>

  <p class="stat stat--paid">$209M paid out by<br>US victims in Q1/2016*</p>
  <p class="stat stat--hit">38% of companies hit by<br>ransomware in 2016*</p>
  <p class="stat stat--sector">38% and 17% of ransomware attacks<br>target the service and manufacturing<br>industries, respectively</p>

  <p class="body-copy body-copy--ransom">Tovrel’s playbook provides actionable instructions for orchestrating and automating ransomware and CipherLock security incident remediation. Specifically, the workflow remediates devices affected by the CipherLock virus, then blocks the ransomware’s lateral and upward propagation, thereby protecting the enterprise network. Suspected ransomware attempts will immediately trigger the playbook to automatically initiate remediation and mitigation procedure</p>

  <section class="banner banner--domain"><h2>Unauthorized Domain Admin Access</h2></section>

  <p class="body-copy body-copy--domain">The talented individuals running your IT department already have a full schedule of important tasks and duties to take care of. What if there was an automated tool that could offload the process of managing domain access while also making it faster, easier and more effective? The right automation playbook can provide actionable instructions for orchestrating and automating responses around unauthorized creation of new domain admin users.</p>

  <svg class="network" width="220" height="190" viewBox="455 690 220 190" aria-hidden="true">
    <g stroke="#0292cd" stroke-width="3" fill="none">
      <line x1="510" y1="724" x2="562" y2="730"/>
      <line x1="541" y1="779" x2="572" y2="758"/>
      <line x1="597" y1="777" x2="594" y2="820"/>
    </g>
    <g fill="#fff" stroke="#0292cd" stroke-width="5">
      <circle cx="486" cy="721" r="24"/>
      <circle cx="600" cy="736" r="38"/>
      <circle cx="521" cy="793" r="20"/>
      <circle cx="594" cy="841" r="21"/>
    </g>
    <circle cx="600" cy="736" r="28" fill="#0292cd" opacity=".85"/>
    <g fill="#fff" stroke="#333" stroke-width="1.6">
      <rect x="478" y="713" width="12" height="15"/><rect x="481" y="710" width="12" height="15"/><rect x="484" y="707" width="12" height="15"/>
      <rect x="514" y="787" width="10" height="12"/><rect x="517" y="784" width="10" height="12"/>
      <rect x="587" y="835" width="10" height="12"/><rect x="590" y="832" width="10" height="12"/>
    </g>
  </svg>

  <section class="banner banner--deface"><h2>Remediating Website Defacement</h2></section>

  <p class="body-copy body-copy--intro">You’ve worked hard to ensure your website accurately represents the quality and commitment that your organization has to offer. With just one breach in your security, all of that could be lost, resulting in costly damage to your brand reputation and a deluge of other technical problems.</p>

  <p class="did-you-know">Did you know<br>there have been at least<br><strong>50,000</strong> successful<br>website defacement attacks<br>each month for the past year,<br>and that <strong>55%</strong> of successful attacks<br>are actually re-defacements? *</p>

  <div class="body-copy body-copy--deface">
    <p>Website defacement is a serious problem, and something that businesses must take proactive measures to prevent.</p>
    <p>The right security playbook can rapidly automate recovery from defacement, and quickly correct any problems that occurred. Tovrel’s playbook instantly and automatically responds to a suspected defacement attack by initiating immediate remediation and mitigation procedures.</p>
  </div>

  <footer class="footer">
    <p class="footer__left">To see full details of playbook, visit our website: tovrel.example</p>
    <p class="footer__right">*To see full details of playbooks, visit our website: tovrel.example<br>*Data and statistics obtained from DefaceWatch.example, NCB, and Trainwell Survey of 1,138 companies, Norvale.</p>
  </footer>
</main>
</body>
</html>
```